Petroleum Trading Company Biz Card

We are a physical trading company for petroleum products such as diesel and gasoline. We need our business cards revamped and the designer is welcome to refine the logo as well. I included png and ai files of the current logo as well as PDF of the current card layout. The card just looks to amateurish (wrong fonts, bad layout etc). The logo is decent but we are open to adjustments to it as well.
Target Market(s)
trading, finance
Contact Information for Business Card
Professional looking card is a must. Clean crisp design and layout. Thanks
Colors
Designer to choose colors to be used in the design.
Look and feel

```html
<!DOCTYPE html>
<html lang="en">
<head>
<meta charset="utf-8">
<title>Meridian Fuels – Business Card</title>
<link rel="stylesheet" href="https://fonts.googleapis.com/css2?family=Roboto+Condensed:wght@300;400;700&family=Varela+Round&display=swap">
<style>
  :root{
    --stage:#6f7b8e;
    --card:#f4f5f6;
    --tint:#cfeaf3;
    --rule:#19a2e2;
    --band-light:#1ea6dd;
    --band-mid:#1d78be;
    --band-dark:#0e3f86;
    --brand:#1f6fb8;
    --ink:#3a3d42;
    --ink-soft:#5a5e64;
  }
  *{box-sizing:border-box;margin:0;padding:0}
  html,body{width:1200px;height:810px;overflow:hidden}
  body{background:var(--stage);position:relative;font-family:"Roboto Condensed",sans-serif}
  .card{position:absolute;top:250px;width:540px;height:310px;background:var(--card);overflow:hidden;box-shadow:0 10px 24px rgba(20,30,50,.35)}
  .card--front{left:30px}
  .card--back{left:630px}
  .card__tint{position:absolute;inset:0}
  .holder{position:absolute;left:34px;top:28px}
  .holder__name{font-weight:700;font-size:24px;color:var(--ink);letter-spacing:.2px}
  .holder__title{font-weight:300;font-size:14px;color:var(--ink-soft);margin-top:2px}
  .holder__dash{position:absolute;left:-16px;top:8px;width:6px;height:18px;background:var(--rule)}
  .rule{position:absolute;left:0;right:0;top:138px;height:3px;background:var(--rule)}
  .brand{position:absolute;display:flex;align-items:center;gap:10px;font-family:"Varela Round",sans-serif;color:var(--brand)}
  .card--front .brand{right:34px;top:60px;font-size:22px}
  .card--back .brand{left:50%;top:50%;transform:translate(-50%,-50%);font-size:30px;gap:14px}
  .brand__dot{width:26px;height:26px;border-radius:50%;background:var(--brand)}
  .card--back .brand__dot{width:36px;height:36px}
  .address{position:absolute;left:34px;top:158px;font-weight:300;font-size:14px;line-height:19px;color:var(--ink)}
  .office-phone{position:absolute;right:40px;top:175px;font-weight:300;font-size:19px;color:var(--ink)}
  .band{position:absolute;left:0;right:0;bottom:0;height:76px}
  .band__main{position:absolute;left:0;right:0;top:0;height:56px;background:linear-gradient(90deg,var(--band-light),var(--band-mid));display:flex;align-items:center;justify-content:space-between;padding:0 30px}
  .band__base{position:absolute;left:0;right:0;bottom:0;height:20px;background:var(--band-dark)}
  .contact{display:flex;align-items:center;gap:7px;color:#fff;font-weight:300;font-size:13px}
  .contact__icon{width:18px;height:18px;border-radius:50%;background:#2b2f36;display:flex;align-items:center;justify-content:center}
</style>
</head>
<body>

<section class="card card--front">
  <svg class="card__tint" width="540" height="310" viewBox="0 0 540 310" aria-hidden="true">
    <polygon points="0,0 330,0 150,138 0,138" fill="var(--tint)"/>
  </svg>
  <div class="holder">
    <span class="holder__dash"></span>
    <p class="holder__name">Daniel Hartwell</p>
    <p class="holder__title">Integrative Bodyworker</p>
  </div>
  <div class="brand"><span class="brand__dot"></span>Meridian Fuels, LLC</div>
  <div class="rule"></div>
  <p class="address">2400 Harbor Point Drive<br>Suite 1800<br>Tampa, FL 33602</p>
  <p class="office-phone">555.204.7719</p>
  <div class="band">
    <div class="band__main">
      <span class="contact"><span class="contact__icon"><svg width="10" height="10" viewBox="0 0 24 24"><path fill="#fff" d="M6.6 10.8a15 15 0 0 0 6.6 6.6l2.2-2.2a1 1 0 0 1 1-.25 11.4 11.4 0 0 0 3.6.57 1 1 0 0 1 1 1V20a1 1 0 0 1-1 1A17 17 0 0 1 3 4a1 1 0 0 1 1-1h3.5a1 1 0 0 1 1 1c0 1.25.2 2.45.57 3.57a1 1 0 0 1-.25 1z"/></svg></span>800.555.0142</span>
      <span class="contact"><span class="contact__icon"><svg width="10" height="10" viewBox="0 0 24 24"><rect x="6" y="2" width="12" height="20" rx="2" fill="#fff"/><rect x="8" y="5" width="8" height="12" fill="#2b2f36"/></svg></span>555.310.2287</span>
      <span class="contact"><span class="contact__icon"><svg width="10" height="10" viewBox="0 0 24 24"><rect x="2" y="5" width="20" height="14" rx="2" fill="#fff"/><path d="M3 6l9 7 9-7" stroke="#2b2f36" stroke-width="2" fill="none"/></svg></span>dhartwell@meridianfuels.example</span>
    </div>
    <div class="band__base"></div>
  </div>
</section>

<section class="card card--back">
  <svg class="card__tint" width="540" height="310" viewBox="0 0 540 310" aria-hidden="true">
    <polygon points="0,0 540,0 540,40 0,240" fill="var(--tint)"/>
  </svg>
  <div class="brand"><span class="brand__dot"></span>Meridian Fuels, LLC</div>
</section>

</body>
</html>
```